Quokka Kitchen logo

I am a catering and food business that requires a logo for my website and all related business branding. I also need a label for my hot sauce. You can find my information on Facebook and there is a picture of the logo I currently use and also a bottle of my hot sauce.
I am based in the Adelaide Hills in South Australia. I would like to use black and gold or Purple and gold my colour scheme and really like the hornet cartoon that I currently use. Something more refined and original would be great...
Industry/Entity Type
Catering
Look and feel
Each slider illustrates characteristics of the customer's brand and the style your logo design should communicate.

```html
<!DOCTYPE html>
<html lang="en">
<head>
<meta charset="utf-8">
<title>Stinger Sauce – label range</title>
<link href="https://fonts.googleapis.com/css2?family=Saira:wght@600;800&family=Oswald:wght@400;500&display=swap" rel="stylesheet">
<style>
  :root{
    --page:#ffffff;
    --paper:#e6e5e2;
    --paper-shade:#d6d5d1;
    --ink:#2a2a2a;
    --white:#f4f4f2;
    --gold:#e0a92a;
    --chilli:#b93230;
    --chilli-deep:#a3282a;
    --night:#1f1f1f;
    --night-soft:#2c2b2b;
    --ember:#7a2a1e;
    --alert:#cf3a2c;
  }
  *{box-sizing:border-box;margin:0;padding:0}
  html,body{width:1200px;height:1000px;overflow:hidden;background:var(--page)}
  body{font-family:"Oswald",sans-serif;color:var(--ink)}
  .range{position:relative;width:1200px;height:1000px;display:flex;justify-content:center;align-items:center;gap:60px}
  .label{position:relative;width:300px;height:560px;background:linear-gradient(180deg,var(--paper),var(--paper-shade));overflow:hidden}
  .label--red{--panel:var(--chilli);--panel-2:var(--chilli-deep);--tag:var(--gold);--lead:var(--gold);--meta:var(--white)}
  .label--ember{--panel:var(--night);--panel-2:var(--ember);--tag:var(--gold);--lead:var(--gold);--meta:var(--gold)}
  .label--night{--panel:var(--night);--panel-2:var(--night-soft);--tag:var(--alert);--lead:var(--alert);--meta:var(--alert)}

  .brand-mark{position:absolute;left:50%;top:28px;transform:translateX(-50%);width:74px;height:74px;border-radius:50%;border:1.5px solid var(--ink);display:flex;align-items:center;justify-content:center;text-align:center}
  .brand-mark span{font-family:"Saira",sans-serif;font-weight:600;font-size:11px;line-height:1.1;color:var(--ink)}

  .panel{position:absolute;left:0;right:0;top:120px;height:355px;padding-top:58px;text-align:center;
    background:radial-gradient(ellipse at 35% 55%,var(--panel-2),var(--panel) 70%);
    clip-path:polygon(0 4%,6% 2.5%,11% 4.5%,17% 1.5%,24% 3.5%,31% 1%,38% 3%,45% 0.5%,52% 2.5%,60% 1%,67% 3.5%,74% 1.5%,81% 4%,88% 2%,94% 3.5%,100% 1.5%,
      100% 96%,94% 98.5%,88% 96.5%,81% 99%,74% 97%,67% 99.5%,60% 97.5%,52% 99%,45% 96.5%,38% 98.5%,31% 97%,24% 99.5%,17% 97.5%,11% 99%,6% 96.5%,0 98.5%)}
  .tagline{font-family:"Saira",sans-serif;font-weight:600;font-size:10.5px;letter-spacing:1.5px;text-transform:uppercase;color:var(--tag)}
  .product-name{margin-top:8px;font-family:"Saira",sans-serif;font-weight:800;font-size:42px;line-height:0.95;letter-spacing:2px;text-transform:uppercase;color:var(--white)}
  .rule{width:190px;height:1px;margin:8px auto 6px;background:var(--tag);opacity:.8}
  .uses{font-family:"Oswald",sans-serif;font-weight:500;font-size:11px;line-height:1.25;text-transform:uppercase;color:var(--white)}
  .uses strong{display:block;font-weight:500;font-size:14px;color:var(--lead)}
  .facts{width:174px;margin:16px auto 0;padding:7px 8px 6px;border:1px solid rgba(255,255,255,.45);font-size:7.5px;line-height:1.35;text-transform:uppercase;text-align:left;color:var(--white)}
  .facts .volume{display:block;text-align:center;margin-top:5px;font-size:10px}
  .origin{margin-top:14px;font-size:10px;line-height:1.3;text-transform:uppercase;color:var(--meta)}

  .footer{position:absolute;left:0;right:0;bottom:0;height:85px;display:flex;align-items:center;justify-content:center;gap:8px;padding-top:10px}
  .footer .dot{width:26px;height:26px;border-radius:50%;border:1px solid var(--ink);display:flex;align-items:center;justify-content:center;font-family:"Saira",sans-serif;font-weight:600;font-size:5px;text-align:center;line-height:1}
  .address{font-size:8.5px;letter-spacing:.5px;text-transform:uppercase}
</style>
</head>
<body>
<main class="range">

  <article class="label label--red">
    <div class="brand-mark"><span>Quokka<br>Kitchen</span></div>
    <section class="panel">
      <p class="tagline">Southern Australia's Finest</p>
      <h1 class="product-name">Stinger<br>Sauce</h1>
      <div class="rule"></div>
      <p class="uses">Hot sauce, marinade, condiment<strong>&amp; extreme flavour bringer</strong></p>
      <p class="facts">Ingredients: chilli, vinegar, water, sugar, garlic, lemon juice, olive oil, spices, cornflour, salt.<span class="volume">250 ML</span></p>
      <p class="origin">Product of Australia<br>Best before: Feb. 2013</p>
    </section>
    <footer class="footer"><span class="dot">Quokka Kitchen</span><span class="address">27 Gully Lane, Bluegum Flat, S.A. 5999</span></footer>
  </article>

  <article class="label label--ember">
    <div class="brand-mark"><span>Quokka<br>Kitchen</span></div>
    <section class="panel" role="img" aria-label="Dark label panel with soft red smoke behind the text">
      <p class="tagline">Southern Australia's Finest</p>
      <h1 class="product-name">Stinger<br>Sauce</h1>
      <div class="rule"></div>
      <p class="uses">Hot sauce, marinade, condiment<strong>&amp; extreme flavour bringer</strong></p>
      <p class="facts">Ingredients: chilli, vinegar, water, sugar, garlic, lemon juice, olive oil, spices, cornflour, salt.<span class="volume">250 ML</span></p>
      <p class="origin">Product of Australia<br>Best before: Feb. 2013</p>
    </section>
    <footer class="footer"><span class="dot">Quokka Kitchen</span><span class="address">27 Gully Lane, Bluegum Flat, S.A. 5999</span></footer>
  </article>

  <article class="label label--night">
    <div class="brand-mark"><span>Quokka<br>Kitchen</span></div>
    <section class="panel">
      <p class="tagline">Southern Australia's Finest</p>
      <h1 class="product-name">Stinger<br>Sauce</h1>
      <div class="rule"></div>
      <p class="uses">Hot sauce, marinade, condiment<strong>&amp; extreme flavour bringer</strong></p>
      <p class="facts">Ingredients: chilli, vinegar, water, sugar, garlic, lemon juice, olive oil, spices, cornflour, salt.<span class="volume">250 ML</span></p>
      <p class="origin">Product of Australia<br>Best before: Feb. 2013</p>
    </section>
    <footer class="footer"><span class="dot">Quokka Kitchen</span><span class="address">27 Gully Lane, Bluegum Flat, S.A. 5999</span></footer>
  </article>

</main>
</body>
</html>
```